Business cards for Remote DBA team

Business cards for team offering database administration, consultation, machine learning and AI services. As of now team is using both
www.korvilnet.cz and www.brestmoorlab.cz URLs

Target Market(s)

IT managers

Industry/Entity Type

It Professional

Contact Information for Business Card

Should include logo
name, email, phone, twitter tag

Font styles to use
Sans Serif

Colors

Designer to choose colors to be used in the design.

```html
<!DOCTYPE html>
<html lang="en">
<head>
<meta charset="utf-8">
<title>Brestmoor Lab – Business Cards</title>
<link rel="stylesheet" href="https://fonts.googleapis.com/css2?family=Lato:wght@400;700;900&display=swap">
<style>
  :root {
    --backdrop: #9e9e9e;
    --card: #ffffff;
    --brand-blue: #1a87c5;
    --ink-grey: #6f6f6f;
    --icon-blue: #1f7fbf;
    --shadow: rgba(0, 0, 0, 0.55);
  }
  * { box-sizing: border-box; margin: 0; padding: 0; }
  html, body {
    width: 1200px;
    height: 900px;
    overflow: hidden;
    background: var(--backdrop);
    font-family: "Lato", Arial, sans-serif;
  }
  .canvas { position: relative; width: 1200px; height: 900px; }

  .card {
    position: absolute;
    top: 200px;
    width: 310px;
    height: 502px;
    background: var(--card);
    box-shadow: 3px 3px 4px var(--shadow);
  }
  .card--front { left: 253px; border-radius: 62px 0 62px 0; }
  .card--back  { left: 627px; border-radius: 0 62px 0 62px; }

  .brand {
    position: absolute;
    display: flex;
    align-items: center;
    gap: 12px;
  }
  .card--front .brand { left: 56px; top: 128px; }
  .card--back .brand  { left: 44px; top: 213px; }
  .brand__dot {
    width: 48px;
    height: 48px;
    border-radius: 50%;
    background: var(--brand-blue);
    flex: none;
  }
  .brand__name {
    color: var(--brand-blue);
    font-weight: 900;
    font-size: 29px;
    line-height: 30px;
    letter-spacing: 0.2px;
  }

  .holder {
    position: absolute;
    left: 34px;
    top: 328px;
    color: var(--brand-blue);
    font-weight: 700;
    font-size: 18px;
    letter-spacing: 0.3px;
  }
  .contacts {
    position: absolute;
    left: 33px;
    top: 373px;
    list-style: none;
    color: var(--ink-grey);
    font-size: 14.5px;
  }
  .contacts li {
    display: flex;
    align-items: center;
    gap: 4px;
    height: 20px;
  }
  .contacts li.contacts__social { margin-top: 20px; }
  .contacts svg { flex: none; }
  .social-dot {
    width: 17px;
    height: 17px;
    border-radius: 50%;
    background: var(--icon-blue);
    flex: none;
  }
</style>
</head>
<body>
<main class="canvas">
  <section class="card card--front" aria-label="Business card front">
    <div class="brand">
      <span class="brand__dot"></span>
      <p class="brand__name">BRESTMOOR<br>LAB</p>
    </div>
    <h1 class="holder">TOMAS VERHAL</h1>
    <ul class="contacts">
      <li>
        <svg width="13" height="11" viewBox="0 0 13 11" aria-hidden="true">
          <path d="M1 3 Q6.5 -0.5 12 3 L10.5 4.5 L8.8 3.6 L4.2 3.6 L2.5 4.5 Z" fill="var(--icon-blue)"/>
          <rect x="2.5" y="5" width="8" height="5.5" rx="1" fill="var(--icon-blue)"/>
        </svg>
        <span>044-555 018 273</span>
      </li>
      <li>
        <svg width="13" height="10" viewBox="0 0 13 10" aria-hidden="true">
          <rect x="0.5" y="0.5" width="12" height="9" fill="var(--icon-blue)"/>
          <path d="M0.8 0.8 L6.5 5.5 L12.2 0.8" fill="none" stroke="#fff" stroke-width="1.2"/>
        </svg>
        <span>info@brestmoorlab.cz</span>
      </li>
      <li class="contacts__social">
        <span class="social-dot"></span>
        <span>@brestmoorlab</span>
      </li>
    </ul>
  </section>

  <section class="card card--back" aria-label="Business card back">
    <div class="brand">
      <span class="brand__dot"></span>
      <p class="brand__name">BRESTMOOR<br>LAB</p>
    </div>
  </section>
</main>
</body>
</html>
```